A simple Chatterbook Ad (not Chatterbook Page) for weight loss surgery

It’s a simple ad in terms of the text.

The text should say:
Curious about weight loss surgery?
This 30 second quiz will tell you which procedure will suit you best

I'm open to variations in the text if it is thought to enhance the ad.

Targeted towards obese individuals who have been unable to lose weight with diet and exercise. My industry is weight loss surgery – webpage www.marcusbellweather.com.au. Clicking the ad leads to a quiz on my webpage relating to weight loss surgery. Most frequent users of this service are females (75%) between ages of 35 and 55 years.

Successful weight loss surgery can enable individuals who have been unable to lose weight to lose a substantial amount of the excess weight they are carrying to be healthier and happier.

```html
<!DOCTYPE html>
<html lang="en">
<head>
<meta charset="utf-8">
<title>Curious About Weight Loss Surgery? – Marcus Bellweather</title>
<link rel="stylesheet" href="https://fonts.googleapis.com/css2?family=Anton&family=Poppins:wght@400;500&display=swap">
<style>
  :root {
    --bg-light: #f4f6f5;
    --bg-mid: #dfe4e2;
    --bg-shade: #c9cfcd;
    --ink-dark: #454545;
    --ink-grey: #3d3d3d;
    --teal: #14a39b;
    --teal-deep: #0d7f7a;
    --teal-soft: #6fd3cb;
    --white: #ffffff;
  }
  * { margin: 0; padding: 0; box-sizing: border-box; }
  html, body {
    width: 1200px;
    height: 1200px;
    overflow: hidden;
    background: var(--bg-light);
  }
  .ad {
    position: relative;
    width: 1200px;
    height: 1200px;
    overflow: hidden;
    background: var(--bg-light);
    font-family: "Poppins", sans-serif;
  }
  .ad__backdrop {
    position: absolute;
    inset: 0;
    background:
      radial-gradient(ellipse 300px 520px at 600px 560px, rgba(255,255,255,0.9), rgba(255,255,255,0) 70%),
      radial-gradient(ellipse 470px 700px at 600px 620px, var(--bg-mid), rgba(223,228,226,0) 75%),
      radial-gradient(ellipse 180px 260px at 250px 260px, var(--bg-shade), rgba(201,207,205,0) 75%),
      radial-gradient(ellipse 180px 260px at 960px 260px, var(--bg-shade), rgba(201,207,205,0) 75%),
      linear-gradient(180deg, #e9edeb 0%, var(--bg-light) 60%, #f7f8f8 100%);
  }
  .ad__guides {
    position: absolute;
    inset: 0;
    width: 1200px;
    height: 1200px;
  }
  .headline {
    position: absolute;
    left: 0;
    right: 0;
    top: 420px;
    text-align: center;
    font-family: "Anton", sans-serif;
    font-weight: 400;
    text-transform: uppercase;
    line-height: 1.06;
    letter-spacing: 1px;
  }
  .headline__lead {
    display: block;
    font-size: 104px;
    color: var(--ink-dark);
    text-shadow: 0 4px 8px rgba(0,0,0,0.18);
  }
  .headline__focus {
    display: block;
    font-size: 104px;
    color: var(--teal);
    text-shadow: 0 4px 8px rgba(0,0,0,0.16);
  }
  .quiz-pill {
    position: absolute;
    left: 200px;
    top: 656px;
    width: 806px;
    height: 128px;
    border-radius: 64px;
    display: flex;
    align-items: center;
    justify-content: center;
    text-align: center;
    background:
      linear-gradient(180deg, rgba(255,255,255,0.25) 0%, rgba(255,255,255,0) 40%),
      linear-gradient(90deg, var(--teal-soft) 0%, var(--teal) 8%, var(--teal-deep) 16%, var(--teal) 30%, var(--teal) 70%, var(--teal-deep) 84%, var(--teal) 92%, var(--teal-soft) 100%);
    box-shadow: 0 0 0 3px rgba(111,211,203,0.55), 0 8px 18px rgba(13,127,122,0.25);
  }
  .quiz-pill__text {
    color: var(--white);
    font-size: 33px;
    font-weight: 400;
    line-height: 1.32;
  }
  .site-link {
    position: absolute;
    left: 0;
    right: 0;
    top: 810px;
    text-align: center;
    color: var(--ink-grey);
    font-size: 28px;
    font-weight: 400;
  }
  .brand {
    position: absolute;
    right: 40px;
    bottom: 58px;
    display: flex;
    align-items: center;
    gap: 14px;
  }
  .brand__dot {
    width: 34px;
    height: 34px;
    border-radius: 50%;
    background: var(--teal);
  }
  .brand__name {
    font-family: "Poppins", sans-serif;
    font-weight: 500;
    font-size: 30px;
    color: var(--teal-deep);
    text-transform: uppercase;
    letter-spacing: 1px;
  }
</style>
</head>
<body>
  <main class="ad">
    <div class="ad__backdrop" role="img" aria-label="Soft-focus photograph of a slim bare torso in pale grey tones"></div>

    <svg class="ad__guides" viewBox="0 0 1080 1080" aria-hidden="true">
      <g fill="none" stroke="#4fbdb5" stroke-width="5" stroke-dasharray="26 16" stroke-linecap="round">
        <path d="M700 -10 C 715 60, 735 120, 762 160"/>
        <path d="M838 238 C 900 270, 990 300, 1090 320"/>
        <path d="M-10 792 C 110 800, 230 880, 310 1000 C 330 1030, 345 1060, 352 1090"/>
      </g>
      <circle cx="800" cy="192" r="44" fill="none" stroke="#4fbdb5" stroke-width="5"/>
    </svg>

    <h1 class="headline">
      <span class="headline__lead">Curious About</span>
      <span class="headline__focus">Weight Loss Surgery?</span>
    </h1>

    <div class="quiz-pill">
      <p class="quiz-pill__text">This 30 second quiz will tell you which<br>procedure will suit you best.</p>
    </div>

    <p class="site-link">www.marcusbellweather.com.au</p>

    <div class="brand">
      <span class="brand__dot"></span>
      <span class="brand__name">Marcus Bellweather</span>
    </div>
  </main>
</body>
</html>
```